Editorial Website Design for High-End Custom Millwork Firm

Design (no development) for a 5-7 page website for a high-end custom architectural millwork firm. Editorial, magazine-quality aesthetic — think Dwelling Quarterly and top-tier millwork studios (Owen Tallard, Vorko). Full brief, reference sites, and project photography attached. We have uploaded a sample of our photography to use in your design. PLEASE READ PDF DOCUMENT BRIEF!!!

```html
<!DOCTYPE html>
<html lang="en">
<head>
<meta charset="utf-8">
<title>Halden Millwork</title>
<link href="https://fonts.googleapis.com/css2?family=Plus+Jakarta+Sans:wght@400;500;600;700&display=swap" rel="stylesheet">
<style>
:root{
  --accent:#c0622b;
  --ink:#111111;
  --muted:#555555;
  --black:#000000;
  --footer:#222222;
  --white:#ffffff;
  --paper:#f6f3f0;
}
*{margin:0;padding:0;box-sizing:border-box}
html,body{width:1200px;height:4283px;overflow:hidden}
body{position:relative;font-family:"Plus Jakarta Sans",sans-serif;color:var(--ink);background:var(--white)}
.abs{position:absolute}
.btn{position:absolute;background:var(--accent);color:var(--white);font-size:12px;font-weight:600;display:flex;align-items:center;justify-content:center;gap:8px;border-radius:4px}
.photo{position:absolute}
.brand{position:absolute;display:flex;align-items:center;gap:10px;font-weight:700;font-size:24px;letter-spacing:.5px}
.brand .sq{width:30px;height:30px;background:var(--accent)}
.nav{position:absolute;left:486px;top:30px;display:flex;gap:30px;font-size:14px;font-weight:500}
.hero{position:absolute;left:12px;top:80px;width:1176px;height:520px;border-radius:0 0 40px 40px;overflow:hidden;background:linear-gradient(135deg,#6e5a44,#b79c7a 45%,#8a7660)}
.hero-card{position:absolute;left:693px;top:185px;width:482px;height:307px;background:var(--white);border-radius:14px;padding:44px 36px}
.hero-card h1{font-size:39px;line-height:40px;font-weight:600;letter-spacing:-.5px}
.hero-card p{margin-top:20px;font-size:14px;line-height:26px;color:var(--accent)}
.dots{position:absolute;left:878px;top:550px;width:112px;height:52px;background:var(--paper);border-radius:20px 20px 0 0;display:flex;justify-content:center;align-items:center;gap:6px}
.dots i{width:12px;height:12px;border-radius:50%;background:#e5c9b6}
.dots i+i{background:var(--accent)}
.about{position:absolute;left:0;top:600px;width:1200px;height:612px;background:linear-gradient(90deg,#f7f1ec,#fbf9f7 60%,#f3f1ef)}
.eyebrow{font-size:14px;font-weight:500;color:var(--accent);display:flex;align-items:center;gap:12px}
.eyebrow b{display:block;width:32px;height:1.5px;background:var(--accent)}
.about h2{font-size:34px;line-height:40px;font-weight:500;margin-top:12px}
.about p{font-size:13px;line-height:23px;color:var(--muted);margin-top:18px}
.services{position:absolute;left:0;top:1212px;width:1200px;height:1918px;background:var(--black);color:var(--white)}
.center-head{position:absolute;left:0;width:1200px;text-align:center}
.center-head h2{font-size:34px;line-height:40px;font-weight:700;margin-top:14px;letter-spacing:-.5px}
.svc{position:absolute}
.svc h3{font-size:26px;font-weight:600;letter-spacing:-.3px}
.svc p{font-size:13px;line-height:23px;margin-top:14px;font-weight:500}
.more{display:flex;align-items:center;gap:10px;margin-top:18px;font-size:15px;font-weight:600}
.more i{width:40px;height:40px;border-radius:50%;background:var(--accent);display:flex;align-items:center;justify-content:center}
.blog-card{position:absolute;background:var(--white);border-radius:16px;box-shadow:0 2px 24px rgba(0,0,0,.07)}
.meta{font-size:13px;color:var(--muted);display:flex;align-items:center;gap:8px}
.meta b{width:10px;height:10px;background:var(--accent);border-radius:2px}
.blog-card h4{font-size:19px;line-height:27px;font-weight:500;margin-top:16px}
.blog-card .more{font-weight:500;color:var(--ink)}
.footer{position:absolute;left:0;top:3850px;width:1200px;height:433px;background:var(--footer);color:var(--white)}
.footer h5{font-size:17px;font-weight:600}
.footer ul{list-style:none;margin-top:26px;font-size:13px;line-height:32px}
.social{display:flex;gap:14px}
.social i{width:34px;height:34px;border-radius:50%;background:#111}
.contact-row{display:flex;gap:16px;font-size:13px;line-height:22px;margin-bottom:10px}
.contact-row i{width:22px;height:22px;border-radius:4px;background:#3a2a22;flex:none;display:flex;align-items:center;justify-content:center}
</style>
</head>
<body>

<header>
  <div class="brand" style="left:16px;top:22px"><span class="sq"></span>HALDEN MILLWORK</div>
  <nav class="nav"><span>Home</span><span>About</span><span>Projects ▾</span><span>Services</span><span>Process</span><span>Blog</span><span>Contact</span></nav>
  <div class="btn" style="left:1067px;top:19px;width:121px;height:38px">Let's Talk <svg width="14" height="10" viewBox="0 0 14 10"><path d="M1 5h11M8 1l4 4-4 4" stroke="#fff" stroke-width="1.6" fill="none"/></svg></div>
</header>

<section>
  <div class="hero" role="img" aria-label="Boutique retail interior with arched wooden shelving, clothing rails and a round display table"></div>
  <div class="hero-card">
    <h1>Restaurant, retail,<br>and hospitality</h1>
    <p>Lorem Ipsum Is Simply Dummy Text Of The Printing And Typesetting Industry.</p>
    <div class="btn" style="left:35px;top:227px;width:130px;height:44px">Let's Talk <svg width="14" height="12" viewBox="0 0 14 12"><path d="M2 11l5-10 5 10M5 11l2-4 2 4" stroke="#fff" stroke-width="1.4" fill="none"/></svg></div>
  </div>
  <div class="dots"><i></i><i></i></div>
</section>

<section class="about">
  <div class="abs" style="left:18px;top:218px;width:325px;height:324px;border:2px solid var(--accent);border-top:none;border-right:none;border-radius:0 0 8px 8px"></div>
  <div class="photo" role="img" aria-label="Modern kitchen with walnut cabinetry, dark stone island and pendant lights" style="left:32px;top:57px;width:463px;height:471px;border-radius:6px;background:linear-gradient(135deg,#d9d6d0,#a8713b 50%,#3f3a36)"></div>
  <div class="abs" style="left:538px;top:56px;width:580px">
    <div class="eyebrow"><b></b>About Us</div>
    <h2>Halden Millwork is an award-quality custom architectural millwork and cabinetry firm based in Durham</h2>
    <p>Lorem Ipsum is simply dummy text of the printing and typesetting industry. Lorem Ipsum has been the industry's standard dummy text ever since 1966, when designers at Pressline and Alan Verity, the librarian at Old Quay Print Library in Harborough, took a 1914 Tullian translation and scrambled it to make dummy text for Pressline's Body Type sheets.</p>
    <p>It has roots in a piece of classical Latin literature from 45 BC, making it over 2000 years old. Peter Lindqvist, a Latin professor at Westmere College in Ashvale, looked up one of the more obscure Latin words, consectetur, from a Lorem Ipsum passage, and going through the cites of the word in classical literature, discovered the undoubtable source.</p>
  </div>
  <div class="btn" style="left:538px;top:496px;width:146px;height:44px">About More <svg width="14" height="12" viewBox="0 0 14 12"><path d="M2 11l5-10 5 10M5 11l2-4 2 4" stroke="#fff" stroke-width="1.4" fill="none"/></svg></div>
</section>

<section class="services">
  <div class="center-head" style="top:66px">
    <div class="eyebrow" style="justify-content:center"><b></b>Our Services<b></b></div>
    <h2>OUR PASSION FOR WOOD AND<br>OUR OBSESSION FOR QUALITY</h2>
  </div>

  <div class="photo" role="img" aria-label="Lounge with carved wooden screen, sofa and armchairs" style="left:18px;top:258px;width:371px;height:404px;background:linear-gradient(135deg,#7a5636,#3d3b55 60%,#2b3a66)"></div>
  <div class="svc" style="left:441px;top:292px;width:390px">
    <h3>Architectural Woodwork</h3>
    <p>Lorem Ipsum is simply dummy text of the printing and typesetting industry. Lorem Ipsum has been the industry's standard dummy text.</p>
    <div class="more"><i><svg width="14" height="10" viewBox="0 0 14 10"><path d="M1 5h11M8 1l4 4-4 4" stroke="#fff" stroke-width="1.6" fill="none"/></svg></i>See More</div>
  </div>

  <div class="photo" role="img" aria-label="Kitchen with walnut cabinets and dark stone island" style="left:795px;top:521px;width:388px;height:403px;background:linear-gradient(160deg,#e3e0da,#a8703a 55%,#403a36)"></div>
  <div class="svc" style="left:795px;top:972px;width:390px">
    <h3>Residential Furniture</h3>
    <p>Lorem Ipsum is simply dummy text of the printing and typesetting industry. Lorem Ipsum has been the industry's standard dummy text.</p>
    <div class="more"><i><svg width="14" height="10" viewBox="0 0 14 10"><path d="M1 5h11M8 1l4 4-4 4" stroke="#fff" stroke-width="1.6" fill="none"/></svg></i>See More</div>
  </div>

  <div class="photo" role="img" aria-label="Retail store with arched wooden shelving and display tables" style="left:18px;top:770px;width:668px;height:341px;background:linear-gradient(135deg,#6e5a44,#b79c7a 45%,#7f8c80)"></div>
  <div class="svc" style="left:18px;top:1158px;width:680px">
    <h3>Corporate Furniture</h3>
    <p>Lorem Ipsum is simply dummy text of the printing and typesetting industry. Lorem Ipsum has been the industry's standard dummy text.</p>
    <div class="more"><i><svg width="14" height="10" viewBox="0 0 14 10"><path d="M1 5h11M8 1l4 4-4 4" stroke="#fff" stroke-width="1.6" fill="none"/></svg></i>See More</div>
  </div>

  <div class="photo" role="img" aria-label="Reception desk with wooden wall panels and a patterned screen" style="left:715px;top:1251px;width:468px;height:403px;background:linear-gradient(135deg,#4a3526,#7b5334 50%,#c8c2b8)"></div>
  <div class="svc" style="left:715px;top:1716px;width:470px">
    <h3>Exterior Furniture</h3>
    <p>Lorem Ipsum is simply dummy text of the printing and typesetting industry. Lorem Ipsum has been the industry's standard dummy text.</p>
    <div class="more"><i><svg width="14" height="10" viewBox="0 0 14 10"><path d="M1 5h11M8 1l4 4-4 4" stroke="#fff" stroke-width="1.6" fill="none"/></svg></i>See More</div>
  </div>

  <div class="photo" role="img" aria-label="Curved oak cabinet with stone top" style="left:18px;top:1390px;width:238px;height:460px;background:linear-gradient(180deg,#ece6dc,#b89a78 60%,#8c6c4c)"></div>
  <div class="svc" style="left:308px;top:1516px;width:340px">
    <h3>Restaurant, Retail, And Hospitality</h3>
    <p>Lorem Ipsum is simply dummy text of the printing and typesetting industry. Lorem Ipsum has been the industry's standard dummy text.</p>
    <div class="more"><i><svg width="14" height="10" viewBox="0 0 14 10"><path d="M1 5h11M8 1l4 4-4 4" stroke="#fff" stroke-width="1.6" fill="none"/></svg></i>See More</div>
  </div>
</section>

<section>
  <div class="abs" style="left:18px;top:3198px">
    <div class="eyebrow">Blog &amp; News<b></b></div>
    <h2 style="font-size:34px;font-weight:500;margin-top:8px">Latest Blog &amp; News</h2>
  </div>
  <div class="btn" style="left:1059px;top:3218px;width:124px;height:40px">View All <svg width="14" height="10" viewBox="0 0 14 10"><path d="M1 5h11M8 1l4 4-4 4" stroke="#fff" stroke-width="1.6" fill="none"/></svg></div>

  <article class="blog-card" style="left:18px;top:3315px;width:569px;height:475px">
    <div class="photo" role="img" aria-label="Craftsman cutting metal with an angle grinder, sparks flying" style="left:17px;top:17px;width:534px;height:253px;border-radius:8px;background:linear-gradient(135deg,#8d9aa6,#4a5560 50%,#c9824a)"></div>
    <div class="abs" style="left:24px;top:295px;width:500px">
      <div class="meta"><b></b>Dec 22, 2025</div>
      <h4>Most Policies Cover Storm-Related Damage But Not Wear And Tear</h4>
      <div class="more"><i><svg width="14" height="10" viewBox="0 0 14 10"><path d="M1 5h11M8 1l4 4-4 4" stroke="#fff" stroke-width="1.6" fill="none"/></svg></i>Read More</div>
    </div>
  </article>

  <article class="blog-card" style="left:614px;top:3323px;width:569px;height:212px">
    <div class="photo" role="img" aria-label="Workshop with a worker assembling a wooden frame" style="left:12px;top:12px;width:227px;height:188px;border-radius:8px;background:linear-gradient(135deg,#6b5d4f,#c9b79c 60%,#8a8680)"></div>
    <div class="abs" style="left:265px;top:32px;width:280px">
      <div class="meta"><b></b>Dec 22, 2025</div>
      <h4>Protecting Homes One Roof A Time</h4>
      <div class="more"><i><svg width="14" height="10" viewBox="0 0 14 10"><path d="M1 5h11M8 1l4 4-4 4" stroke="#fff" stroke-width="1.6" fill="none"/></svg></i>Read More</div>
    </div>
  </article>

  <article class="blog-card" style="left:614px;top:3570px;width:569px;height:212px">
    <div class="photo" role="img" aria-label="Workbench with tools and a geometric wooden panel" style="left:12px;top:12px;width:227px;height:188px;border-radius:8px;background:linear-gradient(135deg,#7c8a94,#d8cdbb 55%,#b59a6c)"></div>
    <div class="abs" style="left:265px;top:28px;width:280px">
      <div class="meta"><b></b>Dec 22, 2025</div>
      <h4>Built Last Engineere For Protection</h4>
      <div class="more"><i><svg width="14" height="10" viewBox="0 0 14 10"><path d="M1 5h11M8 1l4 4-4 4" stroke="#fff" stroke-width="1.6" fill="none"/></svg></i>Read More</div>
    </div>
  </article>
</section>

<footer class="footer">
  <div class="brand" style="left:18px;top:108px;color:var(--white)"><span class="sq"></span>HALDEN MILLWORK</div>
  <p class="abs" style="left:18px;top:170px;width:290px;font-size:13px;line-height:23px">Lorem Ipsum is simply dummy text of the printing and typesetting industry. Lorem Ipsum has been the industry's standard dummy text ever since 1966.</p>
  <div class="social abs" style="left:18px;top:280px"><i></i><i></i><i></i><i></i></div>

  <div class="abs" style="left:440px;top:98px"><h5>Our Services</h5>
    <ul><li>› Dwelling Quarterly</li><li>› Home Ledger</li><li>› Interior Folio</li><li>› Formwork Daily</li><li>› Residential / Commercial</li></ul></div>
  <div class="abs" style="left:720px;top:98px"><h5>Useful Links</h5>
    <ul><li>› Home</li><li>› About Us</li><li>› Services</li><li>› Pages</li><li>› News</li></ul></div>
  <div class="abs" style="left:922px;top:98px;width:260px"><h5>Contact us</h5>
    <div style="margin-top:26px">
      <div class="contact-row"><i><svg width="10" height="13" viewBox="0 0 10 13"><path d="M5 12S1 7 1 4.5a4 4 0 018 0C9 7 5 12 5 12z" fill="var(--accent)"/></svg></i><span>114 Alder Lane, Brookfield<br>Maine 04010</span></div>
      <div class="contact-row"><i><svg width="12" height="12" viewBox="0 0 12 12"><path d="M2 1h3l1 3-2 1a7 7 0 003 3l1-2 3 1v3c-6 1-10-3-9-9z" fill="var(--accent)"/></svg></i><span>+(555)-0142-7731<br>+(555)-0142-7732</span></div>
      <div class="contact-row"><i><svg width="12" height="10" viewBox="0 0 12 10"><rect x="1" y="1" width="10" height="8" fill="var(--accent)"/><path d="M1 1l5 4 5-4" stroke="#3a2a22" fill="none"/></svg></i><span>hello@haldenworks.example</span></div>
    </div>
  </div>
  <div class="abs" style="left:1140px;top:310px;width:44px;height:44px;border-radius:50%;background:var(--accent);display:flex;align-items:center;justify-content:center"><svg width="12" height="14" viewBox="0 0 12 14"><path d="M6 13V2M1 6l5-5 5 5" stroke="#fff" stroke-width="1.8" fill="none"/></svg></div>
  <p class="abs" style="left:0;top:410px;width:1200px;text-align:center;font-size:13px">Copyright © 2026 <span style="color:var(--accent)">Halden Millworks</span>. All rights reserved by</p>
</footer>

</body>
</html>
```